Jewelry shop redesign

Would like to have my webshop (www.moranti.ee) to be redesigned. The shop system, which is built in AJAX will stay the same (consists of different widgets that can be placed using html), just the surroundings needs a luxurious and clean appearance. Only things needed to keep: facebook like box, new product slideshow (can be redesigned aswell), the 3 links on the top which lead to information pages (can be made into buttons), the footer and of course the shop system widgets. The header picture/logo will need to be a link to homepage, which will be the main part of the design. I am quite keen to the display pic that i have on the fb page www.facebook.com/kiritsapood, can be used to make a logo for the header, but feel free to do whatever, as long as it is CLEAN, SIMPLE, LUXURIOUS. get rid of the calculator...

widgets to use with the design (all not needed):

Product Browser Widget Code:
<div>
<script type="text/javascript" src="http://app.shopvarn.com/script.js?718254" charset="utf-8"></script>
<script type="text/javascript"> xProductBrowser("categoriesPerRow=3","views=grid(3,3) list(10) table(20)","categoryView=grid","searchView=list","style="); </script>
<noscript>Your browser does not support JavaScript. Please proceed to <a href="http://moranti.shopvarn.com">HTML version of Moranti OÜ</a></noscript>
</div>

Bag Widget Code:
<div>
<!- remove layout parameter if you want to position minicart yourself ->
<script type="text/javascript"> xMinicart("style=","layout=attachToCategories"); </script>
</div>

minicart: 
<div> <script type="text/javascript" src="http://app.shopvarn.com/script.js?718254"></script> <script type="text/javascript"> xMinicart("style="); </script> </div>

Categories Tabs Widget Code:
<div>
<script type="text/javascript"> xCategories("style="); </script>
</div>

Categories Menu Widget Code:
<div>
<script type="text/javascript"> xVCategories("style="); </script>
</div>

Search Box Widget Code:
<div>
<script type="text/javascript"> xSearchPanel("style="); </script>
</div>

Target Market(s)

women, avg age 24

Industry/Entity Type

Shop

Requirements
Must have
• fb likebox, new product (UUED TOOTED) slideshow, keep the footer (just the company txt and pics), 3 information pages, shop widgets
Should not have
• the lease calculator.

```html
<!DOCTYPE html>
<html lang="et">
<head>
<meta charset="utf-8">
<title>Moranti – Jewelry Shop</title>
<link href="https://fonts.googleapis.com/css2?family=Source+Sans+3:ital,wght@0,300;0,400;0,600;1,400&family=Great+Vibes&display=swap" rel="stylesheet">
<style>
:root{
  --crimson:#b0134c;
  --crimson-text:#b3134f;
  --topbar:#ebebeb;
  --ink:#333;
  --body:#4a4a4a;
  --muted:#777;
  --btn:#555;
  --btn-dark:#2d2d2d;
  --fb-blue:#5a78b8;
  --footer:#3d3d3d;
  --line:#c9c9c9;
}
*{box-sizing:border-box;margin:0;padding:0}
html,body{width:1062px;height:1200px;overflow:hidden;background:#fff}
body{position:relative;font-family:"Source Sans 3",Arial,sans-serif;color:var(--ink)}
a{color:inherit;text-decoration:none}
.abs{position:absolute}

.top-bar{left:0;top:0;width:1062px;height:38px;background:var(--topbar);border-bottom:1px solid #d8d8d8}
.top-links{right:79px;top:10px;font-size:12.5px;color:#444;display:flex;gap:14px}
.top-links span.sep{color:#666}

.header-band{left:0;top:38px;width:1062px;height:332px;background:linear-gradient(#b8154f,var(--crimson))}
.band-shade{left:0;top:370px;width:1062px;height:60px;background:linear-gradient(#ececec,#fff)}

.brand{left:80px;top:48px;font-size:64px;font-weight:300;color:#fff;letter-spacing:1px}
.tagline{left:290px;top:122px;font-size:13.5px;color:#fff;font-weight:600}

.connect{left:628px;top:66px;font-size:12.5px;font-style:italic;color:#fff}
.social{top:60px;width:28px;height:28px;border-radius:50%;background:#fff}
.search{left:806px;top:59px;width:176px;height:27px;background:#fff;border:1px solid #ddd;border-radius:2px;font-size:11px;color:#aaa;padding:6px 18px}
.search svg{position:absolute;right:10px;top:8px}

.main-nav{top:110px;left:611px;display:flex;align-items:center;font-size:13.5px;color:#fff;font-weight:600}
.main-nav .item{padding:4px 14px;height:26px;line-height:18px}
.main-nav .active{background:#fff;color:var(--ink);border-radius:3px}
.main-nav .sep{margin:0 10px;font-weight:400}

.slider{left:79px;top:159px;width:904px;height:270px;background:#fff;border-radius:4px;box-shadow:0 3px 8px rgba(0,0,0,.25)}
.slider-photo{right:4px;top:4px;width:645px;height:262px;border-radius:2px;background:linear-gradient(90deg,#fbf7f7 0%,#f3e4df 25%,#efd0c8 50%,#f6c9c8 75%,#f4b9bc 100%)}
.slider-title{left:53px;top:50px;font-size:33px;font-weight:300;line-height:42px;color:#3a3a3a}
.btn-view{left:54px;top:147px;width:109px;height:40px;background:var(--btn-dark);border-radius:3px;color:#fff;font-size:17px;font-weight:300;padding:8px 0 0 17px}
.btn-view svg{position:absolute;right:17px;top:14px}
.dots{left:56px;top:209px;display:flex;gap:16px}
.dots i{width:13px;height:13px;border-radius:50%;background:#c6c6c6;display:block}
.dots i.on{background:#333}

.welcome{left:80px;top:456px;font-family:"Great Vibes",cursive;font-size:40px;color:var(--crimson-text)}
.intro{left:79px;top:510px;width:905px;font-size:12px;line-height:20.3px;color:var(--body);text-align:justify}

.divider-l{left:120px;top:623px;width:380px;height:1px;background:linear-gradient(90deg,#fff,var(--line))}
.divider-r{left:562px;top:623px;width:363px;height:1px;background:linear-gradient(90deg,var(--line),#fff)}
.divider-mark{left:514px;top:618px;width:34px;height:10px;border-radius:50%;background:#bdbdbd}

.section-title{left:80px;top:652px;font-size:19px;color:var(--crimson-text)}
.dotted{left:80px;top:697px;width:656px;border-top:2px dotted #999}

.product{width:140px}
.product .name{text-align:center;font-size:12px;color:#444;height:18px}
.product .pic{height:96px;border:2px solid #e6e6e6;border-radius:5px;background:#fff;display:flex;align-items:center;justify-content:center}
.product .pic span{width:90px;height:70px;border-radius:10px;display:block}
.product .actions{margin-top:12px;height:24px;display:flex;border-radius:3px;overflow:hidden;background:linear-gradient(#6a6a6a,#4b4b4b);color:#eee;font-size:11px;box-shadow:0 1px 2px rgba(0,0,0,.3)}
.product .actions a{flex:1;text-align:center;line-height:24px}
.product .actions a+a{border-left:1px solid #333}

.subscribe{left:754px;top:655px;width:230px;height:102px;border:1px solid #f0b9c8;border-radius:4px;background:linear-gradient(#fff 40%,#f2f2f2 40%,#fff 60%)}
.subscribe h3{position:absolute;left:12px;top:8px;font-size:19px;font-weight:400;color:var(--crimson-text)}
.sub-input{left:16px;top:55px;width:201px;height:32px;border:1px solid #ccc;border-radius:3px;background:#fff;font-size:13px;font-style:italic;color:#aaa;padding:6px 10px}
.sub-go{right:5px;top:4px;width:38px;height:22px;border-radius:3px;background:linear-gradient(#888,#5c5c5c);color:#fff;font-style:normal;text-align:center;line-height:22px;font-size:13px}

.fb-box{left:752px;top:777px;width:231px;height:301px;border:1px solid var(--fb-blue);border-radius:4px;background:#fff;overflow:hidden}
.fb-head{left:0;top:0;width:229px;height:39px;background:linear-gradient(#6f8cc9,#5874b3);color:#fff;font-size:12.5px;padding:18px 0 0 52px}
.fb-head .sq{position:absolute;left:22px;top:8px;width:22px;height:22px;background:#fff;border-radius:2px;opacity:.9}
.fb-likes{left:5px;top:57px;font-size:9.5px;color:#666}
.fb-likes b{color:var(--crimson);font-weight:600;font-size:11px}
.fb-like-btn{left:144px;top:54px;width:80px;height:19px;border:1px solid #c8d3ea;background:#eef2fb;font-size:9.5px;color:#3b5998;padding:2px 0 0 8px;border-radius:2px}
.fan{width:46px;text-align:center;font-size:8.5px;color:#666}
.fan span{display:block;height:46px;border:1px solid #ddd;margin-bottom:3px}

.footer{left:0;top:1108px;width:1062px;height:92px;background:var(--footer);color:#ccc}
.footer-links{left:0;width:1062px;top:22px;text-align:center;font-size:12.5px}
.footer-links .sep{margin:0 8px}
.copyright{left:0;width:1062px;top:57px;text-align:center;font-size:12px;color:#bbb}
</style>
</head>
<body>

<header>
  <div class="abs top-bar"></div>
  <nav class="abs top-links"><a>My Account</a><span class="sep">|</span><a>My Wishlist</a><span class="sep">|</span><a>My Cart</a><span class="sep">|</span><a>Check out</a><span class="sep">|</span><a>Logout</a></nav>

  <div class="abs header-band"></div>
  <div class="abs band-shade"></div>

  <a class="abs brand" href="#">Moranti</a>
  <div class="abs tagline">Armastus esimesest silmapilgust</div>

  <div class="abs connect">Connect with us :</div>
  <span class="abs social" style="left:729px" aria-label="Circlebook"></span>
  <span class="abs social" style="left:764px" aria-label="Microblog"></span>
  <div class="abs search">Search
    <svg width="10" height="10" viewBox="0 0 10 10"><circle cx="4" cy="4" r="3" fill="none" stroke="#bbb" stroke-width="1.3"/><line x1="6.2" y1="6.2" x2="9.3" y2="9.3" stroke="#bbb" stroke-width="1.5"/></svg>
  </div>

  <nav class="abs main-nav">
    <a class="item active">HOME</a><span class="sep">|</span>
    <a class="item">ABOUT US</a><span class="sep">|</span>
    <a class="item">PRODUCTS</a><span class="sep">|</span>
    <a class="item">CONTACT US</a>
  </nav>

  <section class="abs slider">
    <div class="abs slider-photo" role="img" aria-label="Smiling young woman wearing earrings in front of soft pink blossoms"></div>
    <h2 class="abs slider-title" style="font-weight:300">Get your<br>Favourite Jewels</h2>
    <a class="abs btn-view">View All
      <svg width="7" height="11" viewBox="0 0 7 11"><path d="M0 0L7 5.5L0 11Z" fill="#fff"/></svg>
    </a>
    <div class="abs dots"><i class="on"></i><i></i><i></i><i></i></div>
  </section>
</header>

<main>
  <h1 class="abs welcome" style="font-weight:400">Welcome</h1>
  <p class="abs intro">At vero eos et accusamus et iusto odio dignissimos ducimus qui blanditiis praesentium voluptatum deleniti atque corrupti quos dolores et quas molestias excepturi sint occaecati cupiditate non provident, similique sunt in culpa qui officia deserunt mollitia animi, id est laborum et dolorum fuga. Et harum quidem rerum facilis est et expedita distinctio. Nam libero tempore, cum soluta nobis est eligendi optio cumque nihil impedit quo minus id quod maxime placeat facere possimus, omnis voluptas assumenda est, omnis dolor repellendus. Temporibus autem quibusdam et aut officiis debitis aut rerum necessitatibus saepe eveniet ut et voluptates.</p>

  <div class="abs divider-l"></div>
  <div class="abs divider-mark" role="img" aria-label="Small flourish ornament"></div>
  <div class="abs divider-r"></div>

  <h2 class="abs section-title" style="font-weight:400">Our Products</h2>
  <div class="abs dotted"></div>

  <div class="abs product" style="left:79px;top:724px"><div class="name">Product Name</div><div class="pic"><span role="img" aria-label="Silver ring with black stones" style="background:linear-gradient(#e4e4e4,#9a9a9a)"></span></div><div class="actions"><a>Add to Cart</a><a>View more</a></div></div>
  <div class="abs product" style="left:252px;top:724px"><div class="name">Product Name</div><div class="pic"><span role="img" aria-label="Silver heart pendant necklace" style="background:linear-gradient(#f6f6f6,#d2d2d2)"></span></div><div class="actions"><a>Add to Cart</a><a>View more</a></div></div>
  <div class="abs product" style="left:424px;top:724px"><div class="name">Product Name</div><div class="pic"><span role="img" aria-label="Pearl drop earrings" style="background:linear-gradient(#f4f4f4,#dcd8cf)"></span></div><div class="actions"><a>Add to Cart</a><a>View more</a></div></div>
  <div class="abs product" style="left:597px;top:724px"><div class="name">Product Name</div><div class="pic"><span role="img" aria-label="Pearl bracelet with silver clasp" style="background:linear-gradient(#f6f4f0,#ddd6cc)"></span></div><div class="actions"><a>Add to Cart</a><a>View more</a></div></div>

  <div class="abs product" style="left:79px;top:919px"><div class="name">Product Name</div><div class="pic"><span role="img" aria-label="Diamond heart pendant" style="background:linear-gradient(#f5f5f5,#cfcfcf)"></span></div><div class="actions"><a>Add to Cart</a><a>View more</a></div></div>
  <div class="abs product" style="left:252px;top:919px"><div class="name">Product Name</div><div class="pic"><span role="img" aria-label="Silver charm bracelet" style="background:linear-gradient(#eee,#a9a9a9)"></span></div><div class="actions"><a>Add to Cart</a><a>View more</a></div></div>
  <div class="abs product" style="left:424px;top:919px"><div class="name">Product Name</div><div class="pic"><span role="img" aria-label="Gold floral hair clip with crystals" style="background:linear-gradient(#f7efd9,#d8bf82)"></span></div><div class="actions"><a>Add to Cart</a><a>View more</a></div></div>
  <div class="abs product" style="left:597px;top:919px"><div class="name">Product Name</div><div class="pic"><span role="img" aria-label="Red velvet ring box with purple pouch" style="background:linear-gradient(#7a2f6d,#c4121c)"></span></div><div class="actions"><a>Add to Cart</a><a>View more</a></div></div>
</main>

<aside>
  <div class="abs subscribe">
    <h3>Subscribe Now</h3>
    <div class="abs sub-input">Enter your mail ID<span class="abs sub-go">Go</span></div>
  </div>

  <div class="abs fb-box">
    <div class="abs fb-head"><span class="sq"></span>Find us on Circlebook</div>
    <div class="abs fb-likes">347 people like <b>Moranti</b></div>
    <div class="abs fb-like-btn">Like</div>

    <div class="abs fan" style="left:5px;top:84px"><span role="img" aria-label="Fan avatar" style="background:#5fa7cf"></span>Liina</div>
    <div class="abs fan" style="left:62px;top:84px"><span role="img" aria-label="Fan avatar" style="background:#a85a3a"></span>Marten</div>
    <div class="abs fan" style="left:120px;top:84px"><span role="img" aria-label="Fan avatar" style="background:#7f9a5c"></span>Tarvo</div>
    <div class="abs fan" style="left:177px;top:84px"><span role="img" aria-label="Fan avatar" style="background:#e6dcdc"></span>Kaspar</div>

    <div class="abs fan" style="left:5px;top:152px"><span role="img" aria-label="Fan avatar" style="background:#3a3a3a"></span>Reinu</div>
    <div class="abs fan" style="left:62px;top:152px"><span role="img" aria-label="Fan avatar" style="background:#8a8f98"></span>Oskar</div>
    <div class="abs fan" style="left:120px;top:152px"><span role="img" aria-label="Fan avatar" style="background:#efefef"></span>Villem</div>
    <div class="abs fan" style="left:177px;top:152px"><span role="img" aria-label="Fan avatar" style="background:#9b9b9b"></span>Rasmus</div>

    <div class="abs fan" style="left:5px;top:219px"><span role="img" aria-label="Fan avatar" style="background:#5fa7cf"></span>Liina</div>
    <div class="abs fan" style="left:62px;top:219px"><span role="img" aria-label="Fan avatar" style="background:#a85a3a"></span>Marten</div>
    <div class="abs fan" style="left:120px;top:219px"><span role="img" aria-label="Fan avatar" style="background:#7f9a5c"></span>Tarvo</div>
    <div class="abs fan" style="left:177px;top:219px"><span role="img" aria-label="Fan avatar" style="background:#e6dcdc"></span>Kaspar</div>
  </div>
</aside>

<footer class="abs footer">
  <nav class="abs footer-links"><a>Home</a><span class="sep">|</span><a>About</a><span class="sep">|</span><a>Producs</a><span class="sep">|</span><a>Contact</a><span class="sep">|</span><a>My Account</a><span class="sep">&nbsp;|&nbsp;</span><a>My Wishlist</a><span class="sep">&nbsp;|&nbsp;</span><a>My Cart</a><span class="sep">&nbsp;|&nbsp;</span><a>Check out</a><span class="sep">&nbsp;|&nbsp;</span><a>Logout</a></nav>
  <div class="abs copyright">Copyright © 2012 www.moranti.com &nbsp;&nbsp;All rights reserved.</div>
</footer>

</body>
</html>
```